We need a design for our website called Mivelda which is a brazilian e-commerce focused on childrenswear. Basically your are able to swap (sell & buy) your kids outgrown clothes in the website and we will offer all the necessary services to help you on that.

We believe the main characteristic of the company is the swap of clothes and accessories, but we also feel that by doing this we are guaranteeing that this clothes are not going to trash, reducing clothes waste and being friendly with the environment.

We believe it should be clean with solid and soft colors (refer to the logo attached) and should communicate high quality standards and trust.

We need 2 web pages: home/search results and product details. In both pages we would like to have a fixed top bar with the logo, menu (Buy, Sell, About Us), login, a short message and shopping cart. As well as a footer on the botton with different options and social network links.

- Home/search results: right at the beginning of the page we would like to have a welcome/explanatory carousel banner. It should be a conventional 2 columns design with filters on the left (~25%) and the results on the main section (~3/4 products per row). We need filters for clothes and accessories (size,category, brands, color, gender).

- Product details: again, this should be very clean, with breadcrumbs on the top, a very short description (product's name, category, size), price, "Add to cart" button, an image with zoom functionality (as reference: jquery jqzoom), a "Similar Items" box and a share bar (chatloom, quibbly, snapquilt, v+).

Please bear in mind that we plan to use the main template in different colors across the website.
Updates

Hi everyone! 

We have just updated the brief to add some "Must have features" and "Nice to have features". Please take a careful look at it as it affects pretty much every design we received so far.

We will guarantee the project in the next 1-2 days, but we first would like to see some initial proposals for the second page (product details). Some of you guys are doing an awesome job in the home page!

Best,

Mivelda team

We have just updated the contest payment status: it is now committed!

Best,
Mivelda Team

Target Market(s)

The main audience will be parents of any age

Industry/Entity Type

E-Commerce

Requirements
Must have
• We would like to have only the following elements in the header: logo, login, cart image, Home, "Compre" (Buy), "Venda" (Sell) - not necessarily in this order
- The header should be persistent all over the website (always fixed at the top), thus, if it is too thick it will end up eating too much vertical space in some pages
- The current page should be somehow highlited in the header
- Right next to the cart image on the top we need a small tag indicating how many itens are already inside the cart
- We need a button "Entenda como funcionamos" (which in english means "Learn more") in the banner
- Please use an image of childrens in the banner (not clothes or teenagers)
- Besides the banner, the user in a1024x768 screen resolution should at least be able to view the first row of search results
- There is no need for a "Add to cart" button in every search result (keep price, size, type only). This option should only be available in the second page (product details)
- When needed use "Adicionar ao carrinho" (portuguese) instead of "Add to cart" (english)
- Regarding social network links in the footer, we only need chatloom, quibbly, snapquilt, v+
- In the search results page we need an option to show 12, 24, 48 results per page
- Users need to be able to sort the results (newest first, price low-high and high-low)
Nice to have
• We don´t need a text search box anywhere in the website
- There is no need to present the payment methods in neither pages
- The image of the cart should be modified when there are items inside (full vs empty)
- When the user moves the mouse over the cart image, a simple "div" should show up bellow it listing all items
- Regarding social network links, we like icons that change colors when the user
moves the mouse over them
- Regarding the color scheme, use up to a max of 3 colors and feel free to change the logo colors if you find a better combination than the ones we provided

```html
<!DOCTYPE html>
<html lang="en">
<head>
<meta charset="utf-8">
<title>Mivelda – Buy and save a lot</title>
<link href="https://fonts.googleapis.com/css2?family=Ubuntu:wght@300;400;500;700&family=Arimo:wght@400;700&family=Gelasio&display=swap" rel="stylesheet">
<style>
:root{
  --bar:#3a3a3a;
  --bar-dark:#2a2a2a;
  --accent:#ef5a2c;
  --green:#3aa935;
  --blue:#2d86d3;
  --price:#e6452c;
  --text:#555;
  --muted:#888;
  --line:#e2e2e2;
  --sky-top:#3d9ae8;
  --sky-bottom:#d8ecfb;
  --cta:#d51f1a;
}
*{box-sizing:border-box;margin:0;padding:0}
html,body{width:1094px;height:1200px;overflow:hidden;background:#fff}
body{position:relative;font-family:Arimo,Arial,sans-serif;color:var(--text)}
.abs{position:absolute}

/* header */
.topbar{position:absolute;left:0;top:0;width:1094px;height:50px;background:linear-gradient(#474747,var(--bar-dark));z-index:5}
.brand{left:137px;top:9px;font-family:Ubuntu,sans-serif;font-weight:400;font-size:29px;color:#5cc7d6;letter-spacing:.5px}
.tagline{left:265px;top:20px;font-family:Gelasio,serif;font-size:11px;color:#cfcfcf}
.nav a{position:absolute;top:0;height:50px;line-height:54px;font-weight:700;font-size:12.5px;color:#fff;text-decoration:none}
.nav .current{left:516px;width:50px;text-align:center;background:var(--accent)}
.login{left:826px;top:20px;font-size:12.5px;color:#fff}
.cart{left:887px;top:12px;width:69px;height:28px;border-radius:3px;background:linear-gradient(#4dc142,#2e9a2a);color:#fff;font-weight:700;font-size:12.5px}
.cart svg{position:absolute;left:6px;top:6px}
.cart span{position:absolute;left:36px;top:7px}
.badge{left:945px;top:7px;width:22px;height:12px;background:#fff;border-radius:2px;color:var(--accent);font-size:8px;text-align:center;line-height:12px}

/* hero */
.hero{left:0;top:50px;width:1094px;height:330px;background:radial-gradient(ellipse at 60% 30%,#7cc0f3 0%,var(--sky-top) 45%,#5aa9ea 70%,var(--sky-bottom) 100%)}
.hero h1{position:absolute;left:135px;top:78px;font-family:Ubuntu,sans-serif;font-weight:400;font-size:35px;color:#fff;letter-spacing:-.3px}
.hero p{position:absolute;left:137px;top:140px;width:270px;font-size:11.5px;line-height:18px;color:#222}
.cta{position:absolute;left:137px;top:209px;width:231px;height:34px;border-radius:3px;background:linear-gradient(#ef3b2d,var(--cta));color:#fff;font-family:Ubuntu,sans-serif;font-weight:500;font-size:17px;text-align:center;line-height:34px;box-shadow:0 2px 3px rgba(0,0,0,.3)}
.kids{position:absolute;left:487px;top:27px;width:479px;height:299px;border-radius:40px 40px 0 0;background:linear-gradient(90deg,rgba(231,96,48,.55),rgba(234,205,67,.55) 45%,rgba(200,40,60,.5) 75%,rgba(40,90,200,.55))}
.stripe{left:0;top:380px;width:1094px;height:9px;background:linear-gradient(90deg,#1bb24b 0 12%,#f7941d 12% 24%,#4a86e8 24% 36%,#b5d30f 36% 48%,#1346c1 48% 60%,#ffe600 60% 72%,#22d12e 72% 84%,#5bc9f0 84% 88%,#f47a26 88% 96%,#4a86e8 96%)}

/* sidebar */
.side-title{left:138px;top:415px;font-family:Ubuntu,sans-serif;font-weight:300;font-size:17px;color:var(--blue)}
.search{left:137px;top:451px;width:202px;height:24px;border:1px solid var(--line);border-radius:2px;box-shadow:0 1px 2px rgba(0,0,0,.15);font-size:10px;color:#aaa;padding:6px 8px}
.search-btn{left:312px;top:451px;width:28px;height:24px;background:var(--green);border-radius:0 2px 2px 0}
.perpage{left:138px;top:502px;height:25px;display:flex;box-shadow:0 1px 2px rgba(0,0,0,.2);border-radius:2px}
.perpage span{width:27px;text-align:center;line-height:25px;font-size:10px;font-weight:700;color:#666;background:#fff;border-right:1px solid var(--line)}
.perpage .on{background:var(--green);color:#fff}
.sort{left:230px;top:502px;width:110px;height:25px;box-shadow:0 1px 2px rgba(0,0,0,.2);border-radius:2px;font-size:10.5px;color:#555;padding:6px 8px}
.sort-btn{left:312px;top:502px;width:28px;height:25px;background:var(--green);border-radius:0 2px 2px 0}
.rule{left:137px;width:202px;height:1px;border-top:1px dashed #ddd}
.remove{left:138px;top:566px;font-family:Ubuntu,sans-serif;font-size:13.5px;color:#d42020}
.fhead{left:140px;font-family:Ubuntu,sans-serif;font-size:13.5px;color:var(--blue)}
.fhead i{display:inline-block;margin-right:7px;width:0;height:0;border-style:solid;vertical-align:2px}
.fhead .open{border-width:5px 4px 0 4px;border-color:var(--blue) transparent transparent}
.fhead .closed{border-width:4px 0 4px 5px;border-color:transparent transparent transparent var(--blue)}
.cats{left:154px;top:636px;list-style:none;font-size:10.5px;line-height:17.5px;color:#666;letter-spacing:.2px}
.sizes{left:155px;top:831px;width:184px;height:121px;box-shadow:0 1px 3px rgba(0,0,0,.25);border-collapse:collapse;background:#fff}
.sizes td{border:1px solid #e6e6e6;text-align:center;font-size:11.5px;color:#555;font-weight:700;height:30px}

/* products */
.card{position:absolute;width:132px;height:183px;background:#fff;box-shadow:0 1px 3px rgba(0,0,0,.22)}
.card .ph{position:absolute;left:22px;top:10px;width:88px;height:92px;border-radius:6px}
.card h3{position:absolute;left:12px;top:114px;width:115px;font-size:10px;line-height:12px;font-weight:700;color:#555}
.card .size{position:absolute;left:12px;top:139px;font-size:9.5px;color:var(--muted)}
.card .price{position:absolute;left:12px;top:153px;font-size:14.5px;font-weight:700;color:var(--price)}

.pager{left:727px;top:1094px;font-size:11px;color:#555;display:flex;gap:9px;align-items:center}
.pager .cur{color:var(--price)}
.pager b{color:var(--blue);font-size:9px}

/* footer */
.footer{left:0;top:1137px;width:1094px;height:63px;background:#f4f4f4;border-top:2px solid #ddd}
.copy{left:135px;top:1155px;font-size:10px;color:#555;line-height:18px}
.copy span{color:var(--muted);margin-left:8px}
.social{left:800px;top:1160px;display:flex;gap:12px;font-family:Ubuntu,sans-serif;font-size:11px;color:#8a8a8a}
</style>
</head>
<body>

<header class="topbar">
  <div class="abs brand">Mivelda</div>
  <div class="abs tagline">A short message will go here</div>
  <nav class="nav">
    <a class="current">Home</a>
    <a style="left:588px">Compre</a>
    <a style="left:664px">Vende</a>
    <a style="left:733px">About Us</a>
  </nav>
  <div class="abs login">Login</div>
  <div class="abs cart">
    <svg width="24" height="17" viewBox="0 0 24 17" fill="none" stroke="#fff" stroke-width="1.8"><path d="M1 2h4l3 9h11l3-7H7"/><circle cx="10" cy="14.5" r="1.5" fill="#fff"/><circle cx="18" cy="14.5" r="1.5" fill="#fff"/></svg>
    <span>Cart</span>
  </div>
  <div class="abs badge">02</div>
</header>

<section class="abs hero">
  <h1>Buy and save a lot</h1>
  <p>Lorem ipsum dolor sit amet, consectetur adipiscing elit. Ut urna velit, placerat eu cursus id, tempus eget purus.</p>
  <div class="cta">Entenda como funcionamos</div>
  <div class="kids" role="img" aria-label="Photo of six happy children jumping in colourful clothes"></div>
</section>
<div class="abs stripe"></div>

<aside>
  <div class="abs side-title">Filter Products</div>
  <div class="abs search">Search</div>
  <div class="abs search-btn"><svg width="28" height="24" viewBox="0 0 28 24"><circle cx="12.5" cy="10.5" r="4.5" fill="none" stroke="#fff" stroke-width="2"/><path d="M16 14l5 5" stroke="#fff" stroke-width="2.5"/></svg></div>
  <div class="abs perpage"><span class="on">12</span><span>24</span><span>36</span></div>
  <div class="abs sort">Newest First</div>
  <div class="abs sort-btn"><svg width="28" height="25" viewBox="0 0 28 25"><path d="M9 10h10l-5 6z" fill="#fff"/></svg></div>
  <div class="abs rule" style="top:552px"></div>
  <div class="abs remove"><svg width="9" height="9" viewBox="0 0 9 9" style="margin-right:6px"><path d="M1 1l7 7M8 1l-7 7" stroke="#d42020" stroke-width="2"/></svg>Remove all filter</div>
  <div class="abs rule" style="top:596px"></div>
  <div class="abs fhead" style="top:610px"><i class="open"></i>Category</div>
  <ul class="abs cats"><li>Tops</li><li>Bottoms</li><li>Jackets &amp; Outerwear</li><li>Sporting &amp; Activewear</li><li>Accessories</li><li>Shoes</li></ul>
  <div class="abs rule" style="top:750px"></div>
  <div class="abs fhead" style="top:764px"><i class="closed"></i>Gender</div>
  <div class="abs rule" style="top:792px"></div>
  <div class="abs fhead" style="top:806px"><i class="open"></i>Size</div>
  <table class="abs sizes">
    <tr><td colspan="3" style="padding:0"><table style="width:100%;border-collapse:collapse"><tr><td style="border:0;border-right:1px solid #e6e6e6">12mo</td><td style="border:0;border-right:1px solid #e6e6e6">18mo</td><td style="border:0">24mo</td></tr></table></td></tr>
    <tr><td>2</td><td>3</td><td>4</td><td>5</td></tr>
    <tr><td>6</td><td>7</td><td>8</td><td>10</td></tr>
    <tr><td>12</td><td>14</td><td>16</td><td>18</td></tr>
  </table>
  <div class="abs rule" style="top:974px"></div>
  <div class="abs fhead" style="top:989px"><i class="closed"></i>Price</div>
  <div class="abs rule" style="top:1017px"></div>
  <div class="abs fhead" style="top:1031px"><i class="closed"></i>Color</div>
  <div class="abs rule" style="top:1059px"></div>
  <div class="abs fhead" style="top:1073px"><i class="closed"></i>Brand</div>
  <div class="abs rule" style="top:1101px"></div>
</aside>

<main>
  <div class="card" style="left:376px;top:452px"><div class="ph" role="img" aria-label="Grey short sleeve t-shirt" style="background:#8a8a8a"></div><h3>Shortsleeve CoolWeave T-Shirt</h3><div class="size">Size: 6</div><div class="price">$15</div></div>
  <div class="card" style="left:526px;top:452px"><div class="ph" role="img" aria-label="Navy mesh pants" style="background:#1d2238"></div><h3>Pumora - Kids Boys Mesh Pant</h3><div class="size">Size: 12</div><div class="price">$16</div></div>
  <div class="card" style="left:675px;top:452px"><div class="ph" role="img" aria-label="Red hooded toddler set" style="background:#d42a2a"></div><h3>Maple Lane Bobo 2pc Toddler Set</h3><div class="size">Size: 5</div><div class="price">$20</div></div>
  <div class="card" style="left:825px;top:452px"><div class="ph" role="img" aria-label="Blue sleeveless sports set" style="background:#5aa7d8"></div><h3>2 Piece Sleeveless Sports Set</h3><div class="size">Size: 6</div><div class="price">$8</div></div>

  <div class="card" style="left:376px;top:673px"><div class="ph" role="img" aria-label="Navy knit dress with flowers" style="background:#1f2448"></div><h3>Little Knit Ponte Short Sleeve Dress</h3><div class="size">Size: 2-6x</div><div class="price">$20</div></div>
  <div class="card" style="left:526px;top:673px"><div class="ph" role="img" aria-label="Leopard print tutu dress" style="background:linear-gradient(#8a6a4e,#f2a7c0)"></div><h3>Fair Threads Girls Tutu Dress</h3><div class="size">Size: 4-6x</div><div class="price">$18</div></div>
  <div class="card" style="left:675px;top:673px"><div class="ph" role="img" aria-label="Denim girls dress" style="background:#3e5f86"></div><h3>TOSSA Kids Girls Little Girl Dress</h3><div class="size">Size: 4</div><div class="price">$22</div></div>
  <div class="card" style="left:825px;top:673px"><div class="ph" role="img" aria-label="Lilac glitter dots dress" style="background:#c9a2dc"></div><h3>Princess Lumi “Glitter Dots” Dress</h3><div class="size">Size: 5</div><div class="price">$28</div></div>

  <div class="card" style="left:376px;top:893px"><div class="ph" role="img" aria-label="Turquoise top on hanger" style="background:#2bb3d9"></div><h3>Little Knit Ponte Short Sleeve Dress</h3><div class="size">Size: 2-6x</div><div class="price">$20</div></div>
  <div class="card" style="left:526px;top:893px"><div class="ph" role="img" aria-label="Red printed t-shirt" style="background:#e02a22"></div><h3>Little Knit Ponte Short Sleeve Dress</h3><div class="size">Size: 2-6x</div><div class="price">$20</div></div>
  <div class="card" style="left:675px;top:893px"><div class="ph" role="img" aria-label="Blue top with patterned pants" style="background:linear-gradient(#2aa4d0,#8a5a3a)"></div><h3>Little Knit Ponte Short Sleeve Dress</h3><div class="size">Size: 2-6x</div><div class="price">$20</div></div>
  <div class="card" style="left:825px;top:893px"><div class="ph" role="img" aria-label="Pink polka dot outfit with hat" style="background:#d9588f"></div><h3>Little Knit Ponte Short Sleeve Dress</h3><div class="size">Size: 2-6x</div><div class="price">$20</div></div>

  <div class="abs pager"><b>◀◀</b><b>◀</b><span class="cur">1</span><span>2</span><span>3</span><span>4</span><span>5</span><span>6</span><span>7</span><span>8</span><span>...</span><b>▶</b><b>▶▶</b></div>
</main>

<footer class="abs footer"></footer>
<div class="abs copy">Copyright © 2013 Mivelda. <span>Terms of Use -</span> <span style="margin-left:2px">Privacy Policy</span><br>All rights reserved.</div>
<div class="abs social"><span>chatloom</span><span>quibbly</span><span>v+</span><span>snapquilt</span></div>

</body>
</html>
```